Money transfer app

I want a redesign of 3-4 screens of the mobile app.

I want:
1. Splash screen
2. Welcome screen
3. Login screen
4. More options. to send screen

I have attached existing designs.

```html
<!DOCTYPE html>
<html lang="en">
<head>
<meta charset="utf-8">
<title>swiftsend – app screens</title>
<link rel="stylesheet" href="https://fonts.googleapis.com/css2?family=Outfit:wght@400;500;600&family=Poppins:wght@400;500;600&display=swap">
<style>
  :root{
    --canvas:#000000;
    --splash:#0a3a00;
    --brand-ink:#0d3a05;
    --accent:#7ddc4e;
    --mint:#dcfccc;
    --mint-soft:#e9fde0;
    --btn-top:#1f8f0c;
    --btn-bottom:#0b4700;
    --field-line:#c9d9c0;
    --muted:#5d6b58;
    --white:#ffffff;
  }
  *{box-sizing:border-box;margin:0;padding:0}
  html,body{width:1200px;height:1000px;overflow:hidden;background:var(--canvas)}
  body{position:relative;font-family:"Outfit",sans-serif;color:var(--brand-ink)}
  .screen{position:absolute;overflow:hidden;border-radius:22px}
  .abs{position:absolute}
  .center-x{left:0;right:0;text-align:center}
  .btn{position:absolute;display:flex;align-items:center;justify-content:center;border-radius:10px;font-family:"Poppins",sans-serif;font-weight:500;letter-spacing:.04em}
  .btn-primary{background:linear-gradient(var(--btn-top),var(--btn-bottom));color:var(--white)}
  .btn-secondary{background:var(--mint);color:var(--brand-ink)}
  .brand-mark{display:flex;align-items:center;justify-content:center;gap:8px;font-family:"Outfit",sans-serif;font-weight:600}
  .brand-dot{border-radius:50%;background:var(--accent)}

  /* splash */
  .splash{left:54px;top:280px;width:197px;height:437px;background:var(--splash)}
  .splash .brand-mark{position:absolute;left:0;right:0;top:204px;color:var(--accent);font-size:20px}
  .splash .brand-dot{width:16px;height:16px}

  /* welcome */
  .welcome{left:292px;top:173px;width:299px;height:666px;background:linear-gradient(#ffffff 0%,#d6f9c4 45%,#8de863 100%)}
  .welcome-kicker{top:48px;font-size:17px;font-weight:500}
  .welcome-brand{top:76px;font-size:32px;font-weight:600;letter-spacing:-.01em}
  .welcome-copy{font-size:12px;line-height:20.5px}
  .welcome-art{left:30px;top:275px;width:239px;height:215px;border-radius:28px;background:radial-gradient(circle at 35% 40%,#9fcf8a 0%,#5fae3d 45%,#2f7a1a 100%)}

  /* login */
  .login{left:628px;top:279px;width:203px;height:450px;background:linear-gradient(#ffffff 0%,#ffffff 30%,#c9f7a9 80%,#b4f38c 100%)}
  .login .brand-mark{position:absolute;left:0;right:0;top:96px;font-size:20px;color:var(--brand-ink)}
  .login .brand-dot{width:14px;height:14px}
  .login-title{top:150px;font-size:12px;font-weight:500}
  .field{position:absolute;left:21px;width:160px;height:24px;border:1px solid var(--field-line);border-radius:5px;background:var(--white);font-family:"Poppins",sans-serif;font-size:7px;color:#8a9386;display:flex;align-items:center;padding-left:7px}
  .small{font-family:"Poppins",sans-serif;font-size:5.5px}
  .social{position:absolute;top:343px;width:19px;height:19px;border-radius:50%}

  /* send options */
  .options{left:869px;top:189px;width:297px;height:660px;background:var(--white)}
  .options-head{left:0;top:0;width:297px;height:75px;background:var(--mint);border-radius:0 0 14px 14px}
  .options-title{left:18px;top:33px;font-size:19px;font-weight:500}
  .option-card{position:absolute;left:18px;width:258px;height:111px;border-radius:16px;background:var(--mint)}
  .option-card svg{position:absolute;left:18px;top:32px}
  .option-name{position:absolute;left:79px;top:28px;font-family:"Poppins",sans-serif;font-size:16px;font-weight:600}
  .option-desc{position:absolute;left:79px;top:52px;font-size:11.5px;line-height:17px}
  .tab-bar{left:0;top:605px;width:297px;height:55px;background:var(--mint)}
  .tab{position:absolute;top:10px;width:50px;margin-left:-25px;text-align:center;font-family:"Poppins",sans-serif;font-size:8px;color:var(--muted)}
  .tab svg{display:block;margin:0 auto 3px}
  .tab.active{color:var(--brand-ink);font-weight:600}
</style>
</head>
<body>

<!-- Splash -->
<section class="screen splash">
  <div class="brand-mark"><span class="brand-dot"></span>swiftsend</div>
</section>

<!-- Welcome -->
<section class="screen welcome">
  <p class="abs center-x welcome-kicker">Welcome to</p>
  <h1 class="abs center-x welcome-brand">swiftsend</h1>
  <p class="abs center-x welcome-copy" style="top:142px">Sending Money made Simple,<br>Fast &amp; Transparent</p>
  <p class="abs center-x welcome-copy" style="top:201px">Send money online 24/7<br>When it’s convenient for you</p>
  <div class="abs welcome-art" role="img" aria-label="Illustration of a harbour landmark with sail-shaped roofs under a large moon"></div>
  <div class="btn btn-primary" style="left:28px;top:525px;width:241px;height:37px;font-size:13px">Get Started</div>
  <div class="btn btn-secondary" style="left:28px;top:575px;width:241px;height:37px;font-size:13px">Send Money</div>
</section>

<!-- Login -->
<section class="screen login">
  <div class="brand-mark"><span class="brand-dot"></span>swiftsend</div>
  <p class="abs center-x login-title">Sign In to continue</p>
  <div class="field" style="top:180px">Email Address</div>
  <div class="field" style="top:211px">Password
    <svg class="abs" style="right:6px;top:7px" width="9" height="9" viewBox="0 0 10 10" fill="none" stroke="#7a8576" stroke-width="1"><path d="M1 5c1.5-2.5 6.5-2.5 8 0-1.5 2.5-6.5 2.5-8 0z"/><circle cx="5" cy="5" r="1.3"/><path d="M2 8.5 8 1.5"/></svg>
  </div>
  <p class="abs small" style="left:21px;top:242px;font-weight:600">Forgot password?</p>
  <div class="btn btn-primary" style="left:21px;top:260px;width:163px;height:26px;font-size:8px;border-radius:7px;letter-spacing:.02em">Login</div>
  <p class="abs center-x small" style="top:296px">Not a member? <b>Register now</b></p>
  <div class="abs" style="left:21px;top:314px;width:163px;height:1px;background:#e3ece0"></div>
  <p class="abs center-x small" style="top:326px;color:var(--muted)">Or continue with</p>
  <span class="social" style="left:66px;background:#ea3a4a"></span>
  <span class="social" style="left:92px;background:#1d1d1d"></span>
  <span class="social" style="left:117px;background:#1a6ef0"></span>
</section>

<!-- More options to send -->
<section class="screen options">
  <div class="abs options-head"></div>
  <h2 class="abs options-title">More option to send</h2>

  <div class="option-card" style="top:92px">
    <svg width="40" height="46" viewBox="0 0 40 46" fill="none" stroke="#0d3a05" stroke-width="2.4"><rect x="6" y="3" width="20" height="40" rx="3"/><path d="M6 36h20"/><circle cx="16" cy="40" r="1.2" fill="#0d3a05"/><rect x="18" y="17" width="16" height="12" rx="2" fill="#dcfccc"/><path d="M28 21h6v4h-6z"/></svg>
    <div class="option-name">Mobile Money</div>
    <div class="option-desc">Real-time transfer to<br>mobile wallet</div>
  </div>

  <div class="option-card" style="top:220px">
    <svg width="44" height="46" viewBox="0 0 44 46" fill="#0d3a05"><rect x="2" y="24" width="6" height="16"/><path d="M10 26h10l8 4h9c3 0 3 5 0 5H24v2h14l4-3v5l-8 5H10z"/><g fill="none" stroke="#0d3a05" stroke-width="2.4"><rect x="14" y="6" width="24" height="14" rx="2" transform="rotate(-12 26 13)"/><circle cx="26" cy="13" r="3"/></g></svg>
    <div class="option-name">Cash Pickup</div>
    <div class="option-desc">Pickup from our large<br>network of agents</div>
  </div>

  <div class="option-card" style="top:348px">
    <svg width="42" height="46" viewBox="0 0 42 46" fill="#0d3a05"><rect x="16" y="2" width="10" height="13" rx="1" fill="none" stroke="#0d3a05" stroke-width="2.2"/><path d="M3 20 21 13l18 7v3H3z"/><rect x="6" y="26" width="4" height="12"/><rect x="14" y="26" width="4" height="12"/><rect x="24" y="26" width="4" height="12"/><rect x="32" y="26" width="4" height="12"/><rect x="2" y="40" width="38" height="4"/></svg>
    <div class="option-name">Bank Deposit</div>
    <div class="option-desc">Instant transfer to<br>Bank Account</div>
  </div>

  <div class="btn btn-primary" style="left:29px;top:498px;width:239px;height:37px;font-size:13px">Get Started</div>
  <div class="btn btn-secondary" style="left:29px;top:548px;width:239px;height:37px;font-size:13px">Send Money</div>

  <nav class="abs tab-bar">
    <div class="tab active" style="left:64px"><svg width="16" height="16" viewBox="0 0 16 16" fill="#0d3a05"><path d="M2 7 8 2l6 5v7H2z"/></svg>Home</div>
    <div class="tab" style="left:122px"><svg width="16" height="16" viewBox="0 0 16 16" fill="none" stroke="#5d6b58" stroke-width="1.2"><circle cx="8" cy="8" r="6.5"/><text x="8" y="11" font-size="8" text-anchor="middle" fill="#5d6b58" stroke="none" font-family="Poppins,sans-serif">$</text></svg>Transfer</div>
    <div class="tab" style="left:179px"><svg width="16" height="16" viewBox="0 0 16 16" fill="none" stroke="#5d6b58" stroke-width="1.2"><rect x="2" y="3" width="12" height="11" rx="2"/><path d="M10 7h5v4h-5z"/></svg>Wallet</div>
    <div class="tab" style="left:237px"><svg width="16" height="16" viewBox="0 0 16 16" fill="none" stroke="#5d6b58" stroke-width="1.2"><circle cx="8" cy="8" r="6.5"/><circle cx="8" cy="6.5" r="2.2"/><path d="M4 12.5c1.5-2.5 6.5-2.5 8 0"/></svg>Profile</div>
  </nav>
</section>

</body>
</html>
```